Corporate Business Card

Very professional, Modern, Not to busy, include phone address email, website
(253) 555-0174, 61807 19th Street N, Kent, WA 98517, marcus@kestrelbayholding.com, brelvanindustries.com

Target Market(s)

Manufacturing

Industry/Entity Type

Aero, machining, manufacturing, Off road racing

Contact Information for Business Card

Phone, address email, website

```html
<!DOCTYPE html>
<html lang="en">
<head>
<meta charset="utf-8">
<title>Brelvan Industries – Business Card</title>
<link href="https://fonts.googleapis.com/css2?family=Arimo:wght@400;700&display=swap" rel="stylesheet">
<style>
  :root {
    --navy: #14306a;
    --navy-deep: #0f285c;
    --navy-faint: #1c3c7a;
    --red: #d32a33;
    --paper: #ffffff;
    --ink-grey: #6b6f76;
    --ink-dark: #2a2d33;
    --backdrop: #e6e7ea;
    --divider: #c9ccd2;
  }
  * { margin: 0; padding: 0; box-sizing: border-box; }
  html, body { width: 1200px; height: 874px; overflow: hidden; }
  body {
    background: var(--backdrop);
    font-family: "Arimo", Arial, sans-serif;
    position: relative;
  }
  .card {
    position: absolute;
    left: 290px;
    width: 620px;
    height: 354px;
    border-radius: 4px;
    overflow: hidden;
    box-shadow: 0 6px 18px rgba(0,0,0,0.18);
  }
  /* front */
  .card-front { top: 50px; background: var(--navy); }
  .front-name {
    position: absolute;
    left: 0; right: 0; top: 150px;
    text-align: center;
    font-weight: 700;
    font-size: 46px;
    letter-spacing: 2px;
    color: var(--navy-faint);
  }
  /* back */
  .card-back { top: 470px; background: var(--paper); }
  .brand {
    position: absolute;
    left: 30px; top: 142px;
    width: 250px;
    display: flex; align-items: center; gap: 9px;
    white-space: nowrap;
  }
  .brand-mark { width: 13px; height: 13px; background: var(--red); flex: none; }
  .brand-name {
    font-weight: 700;
    font-size: 21px;
    color: var(--navy);
    letter-spacing: 0.3px;
  }
  .divider {
    position: absolute;
    left: 302px; top: 118px;
    width: 1px; height: 140px;
    background: var(--divider);
  }
  .contact {
    position: absolute;
    left: 322px; top: 116px;
    color: var(--ink-dark);
    white-space: nowrap;
  }
  .person-name {
    font-weight: 700; font-size: 23px;
    color: var(--navy); letter-spacing: 0.5px;
  }
  .person-title {
    font-size: 14px; color: var(--ink-grey);
    margin-top: 2px;
  }
  .address { font-size: 15px; line-height: 19px; margin-top: 12px; }
  .contact-line {
    display: flex; align-items: center; gap: 8px;
    font-size: 15px; line-height: 20px;
  }
  .address + .contact-line { margin-top: 4px; }
  .contact-line svg { width: 12px; height: 12px; flex: none; }
  .footer-bands { position: absolute; left: 0; bottom: 0; width: 620px; height: 80px; }
  .website {
    position: absolute;
    right: 26px; bottom: 14px;
    color: var(--paper);
    font-size: 16px; letter-spacing: 1px;
  }
</style>
</head>
<body>
  <section class="card card-front" aria-label="Card front">
    <div class="front-name">Brelvan Industries</div>
  </section>

  <section class="card card-back" aria-label="Card back">
    <div class="brand">
      <span class="brand-mark"></span>
      <span class="brand-name">Brelvan Industries</span>
    </div>

    <div class="divider"></div>

    <div class="contact">
      <div class="person-name">DANIEL WHITFORD</div>
      <div class="person-title">Managing Director</div>
      <div class="address">61807 19th Street N<br>Kent, WA 98517</div>
      <div class="contact-line">
        <svg viewBox="0 0 12 12" aria-hidden="true"><path d="M2.5 0.8 L4.3 0.8 L5 3.3 L3.8 4.3 Q4.8 6.8 7.7 8.2 L8.7 7 L11.2 7.7 L11.2 9.5 Q11 11.2 9.3 11.2 Q1.2 10.5 0.8 2.5 Q0.8 0.9 2.5 0.8 Z" fill="var(--red)"/></svg>
        <span>(253) 555-0174</span>
      </div>
      <div class="contact-line">
        <svg viewBox="0 0 12 12" aria-hidden="true"><rect x="0.5" y="2" width="11" height="8" fill="var(--red)"/><path d="M0.8 2.4 L6 6.6 L11.2 2.4" fill="none" stroke="#fff" stroke-width="1"/></svg>
        <span>marcus@kestrelbayholding.com</span>
      </div>
    </div>

    <svg class="footer-bands" viewBox="0 0 620 80" aria-hidden="true">
      <polygon points="0,0 390,34 384,40 0,8" fill="var(--red)"/>
      <polygon points="0,13 380,46 400,36 620,36 620,80 0,80" fill="var(--navy-deep)"/>
      <polygon points="0,17 372,49 0,49" fill="var(--paper)"/>
    </svg>
    <div class="website">www.brelvanindustries.com</div>
  </section>
</body>
</html>
```